Business Card design for a skin clinic

i would like a business card design for our skin clinic.
our logo colors are Blue and Grey and Bule /white.
we are searching for a minimalistic design yet very elegant,dynamic and professional which can reflect a professional medical skin care clinic( not a beauty salon).
THE DESGIN IS NOT FOR A PERSON IT WILL BE USED IN THE CLINIC FOR CLIENTS SO THERE SHOULD BE NO NAME OF A PERSON ONLY THE CLINIC NAME AND THE CONTACT INFO

Target Market(s)
young and old womens
Industry/Entity Type
Business
Contact Information for Business Card
we have 2 address and both should be on the card.
address A: Lindenhoflaan 214B, 3041KP Rotterdam, Tel 010 483 21 95
address B: Zonnewijzerstraat 238, 1062RT Amsterdam Tel 020 571 3829
website www.huidpuntzorg.nu, email info@huidpuntzorg.nu
Look and feel
Each slider illustrates characteristics of the customer's brand and the style your logo design should communicate.

```html
<!DOCTYPE html>
<html lang="nl">
<head>
<meta charset="utf-8">
<title>Huidpunt Zorg – visitekaartje</title>
<link rel="stylesheet" href="https://fonts.googleapis.com/css2?family=Source+Sans+3:wght@400;600&family=Montserrat:wght@400;500&display=swap">
<style>
  :root {
    --stage: #e9eaec;
    --card-white: #ffffff;
    --card-navy: #141d26;
    --ink: #1c1f24;
    --icon-tile: #eef0f2;
    --brand-blue: #2f8fd6;
    --brand-grey: #d9dde2;
    --tagline: #c3c9d0;
  }
  * { box-sizing: border-box; margin: 0; padding: 0; }
  html, body { width: 1200px; height: 1000px; overflow: hidden; }
  body {
    background: var(--stage);
    display: flex;
    align-items: center;
    justify-content: center;
    gap: 40px;
    font-family: "Source Sans 3", Arial, sans-serif;
  }
  .card {
    width: 540px;
    height: 310px;
    box-shadow: 0 6px 18px rgba(0,0,0,.18);
    position: relative;
    flex: none;
  }

  /* Contact side */
  .card--contact { background: var(--card-white); padding: 42px 0 0 36px; }
  .contact-list { list-style: none; }
  .contact-row {
    display: flex;
    align-items: center;
    height: 80px;
  }
  .icon-tile {
    flex: none;
    width: 74px;
    height: 80px;
    background: var(--icon-tile);
    display: flex;
    align-items: center;
    justify-content: center;
    border-bottom: 2px solid var(--card-white);
  }
  .icon-tile svg { width: 44px; height: 44px; }
  .contact-main {
    flex: none;
    width: 200px;
    margin-left: 30px;
    font-size: 15px;
    line-height: 1.15;
    color: var(--ink);
  }
  .divider {
    flex: none;
    width: 1.5px;
    height: 32px;
    background: var(--ink);
    margin: 0 20px 0 14px;
  }
  .contact-side { font-size: 15px; color: var(--ink); white-space: nowrap; }

  /* Brand side */
  .card--brand {
    background: var(--card-navy);
    display: flex;
    flex-direction: column;
    align-items: center;
    justify-content: center;
  }
  .brand-name {
    display: flex;
    align-items: center;
    gap: 14px;
    font-family: "Montserrat", Arial, sans-serif;
    font-weight: 500;
    font-size: 34px;
    letter-spacing: 3px;
    color: var(--brand-grey);
    text-transform: uppercase;
  }
  .brand-dot {
    width: 16px;
    height: 16px;
    border-radius: 50%;
    background: var(--brand-blue);
  }
  .brand-tagline {
    margin-top: 14px;
    font-family: "Montserrat", Arial, sans-serif;
    font-size: 13px;
    letter-spacing: 1.5px;
    color: var(--tagline);
  }
</style>
</head>
<body>
  <section class="card card--contact" aria-label="Contactgegevens">
    <ul class="contact-list">
      <li class="contact-row">
        <span class="icon-tile">
          <svg viewBox="0 0 44 44" aria-hidden="true">
            <circle cx="22" cy="22" r="21" fill="var(--brand-blue)"/>
            <path d="M22 12a6.5 6.5 0 0 0-6.5 6.5c0 5 6.5 12.5 6.5 12.5s6.5-7.5 6.5-12.5A6.5 6.5 0 0 0 22 12z" fill="#fff"/>
            <circle cx="22" cy="18.5" r="2.4" fill="var(--brand-blue)"/>
          </svg>
        </span>
        <span class="contact-main">Lindenhoflaan 214B<br>3041KP Rotterdam</span>
        <span class="divider"></span>
        <span class="contact-side">Tel - 010 483 21 95</span>
      </li>
      <li class="contact-row">
        <span class="icon-tile">
          <svg viewBox="0 0 44 44" aria-hidden="true">
            <circle cx="22" cy="22" r="21" fill="var(--brand-blue)"/>
            <path d="M22 12a6.5 6.5 0 0 0-6.5 6.5c0 5 6.5 12.5 6.5 12.5s6.5-7.5 6.5-12.5A6.5 6.5 0 0 0 22 12z" fill="#fff"/>
            <circle cx="22" cy="18.5" r="2.4" fill="var(--brand-blue)"/>
          </svg>
        </span>
        <span class="contact-main">Zonnewijzerstraat 238<br>1062RT Amsterdam</span>
        <span class="divider"></span>
        <span class="contact-side">Tel - 020 571 3829</span>
      </li>
      <li class="contact-row">
        <span class="icon-tile">
          <svg viewBox="0 0 44 44" aria-hidden="true">
            <circle cx="22" cy="22" r="21" fill="var(--brand-blue)"/>
            <rect x="13" y="16" width="18" height="12" rx="1" fill="#fff"/>
            <path d="M13 16.5l9 6.5 9-6.5" fill="none" stroke="var(--brand-blue)" stroke-width="1.4"/>
          </svg>
        </span>
        <span class="contact-main">info@huidpuntzorg.nu</span>
        <span class="divider"></span>
        <span class="contact-side">www.huidpuntzorg.nu</span>
      </li>
    </ul>
  </section>

  <section class="card card--brand" aria-label="Merkzijde">
    <p class="brand-name"><span class="brand-dot" aria-hidden="true"></span>Huidpunt Zorg</p>
    <p class="brand-tagline">clinical care for calm skin</p>
  </section>
</body>
</html>
```